Label Design for Climbing Chalk (fitness category)

I am looking for someone to design a front and back label for a bottle of liquid chalk. Liquid chalk is used in gyms, gymnastics, climbing to prevent your hands from getting moist and increase friction. I'm uploading some design motivations that I like.

The bottle is going to be black and I want the label to be clear. You have free reign of how you want to approach this design. Below are more specifics for the sizing:

*Attached is a picture of a competitor product (Tor Hold Liquid Chalk). Please don't use this for motivation, their label is very bad. I'm attaching a picture so that you can see what the bottle looks like.
*Attached are design motivations that I like
*The bottle is 50 ml, it's 3.75 inches tall, 2 inches wide and 1.25 inches in depth.
*The label can be square or oval (it's up to you). The size of the label needs to be 1,25 x 2.25 inches.
*Name of the product: Varnel Liquid Chalk
*Label needs to have the following Required Text. You can arrange it however you like:
- (50 ml)
- Made by USA Competitive Athletes for Athletes. Increases grip and lasts 3-4 times longer than regular chalk.
- Directions: Shake well. Squeeze some Varnel Liquid Chalk into your hand and rub your hands together. Let your hands air dry for about 10 seconds. To remove the chalk wash your hands with light soap.
Warning: Avoid contact with Eyes. Do not use on broken skin. Do not ingest. Keep out of reach of small children.
- Ingredients: Magnesium carbonate, SD Alcohol, hydroxypropylcellulose, colophonium.

Target Market(s)

Fitness, Athletes, Rock Climbers, Weight Lifters, Gymnasts, etc

Industry/Entity Type

Fitness

Font styles to use
Sans Serif

Colors

Designer to choose colors to be used in the design.

Requirements
Must have
• Please see Project Description for required text. The bottle is going to be black and I want the clear label so please be creative with the colors that would look good
Nice to have
• Please see attached branding ideas that I liked for font and colors. You don't have to strictly stick to them, these are just some of the ones I liked. Be creative and put your best foot forward.

```html
<!DOCTYPE html>
<html lang="en">
<head>
<meta charset="utf-8">
<title>Varnel Liquid Chalk – Front and Back Labels</title>
<link rel="stylesheet" href="https://fonts.googleapis.com/css2?family=Michroma&family=Lato:ital,wght@0,400;0,700;1,700&display=swap">
<style>
  :root {
    --page-bg: #ffffff;
    --label-red: #931b21;
    --label-red-deep: #6a1015;
    --label-red-light: #a8242b;
    --label-ink: #ffffff;
    --print-tone: rgba(255, 255, 255, 0.35);
    --size-tag: #f2a41c;
    --size-tag-ink: #1a1a1a;
    --badge-ring: #ffffff;
    --badge-fill: #c8c8d4;
  }
  * { box-sizing: border-box; margin: 0; padding: 0; }
  html, body { width: 1200px; height: 750px; overflow: hidden; background: var(--page-bg); }
  .canvas {
    width: 1200px; height: 750px;
    display: flex; justify-content: center; align-items: center; gap: 60px;
  }
  .label {
    position: relative;
    width: 300px; height: 540px;
    border-radius: 150px;
    overflow: hidden;
    background: linear-gradient(100deg, var(--label-red-deep) 0%, var(--label-red) 35%, var(--label-red-light) 100%);
    color: var(--label-ink);
  }
  /* front */
  .brand-mark {
    position: absolute; top: 48px; left: 50%; transform: translateX(-50%);
    width: 46px; height: 46px; border-radius: 50%; background: var(--label-ink);
  }
  .brand-name {
    position: absolute; top: 118px; width: 100%; text-align: center;
    font-family: "Michroma", sans-serif; font-size: 24px; letter-spacing: 1px;
  }
  .product-name {
    position: absolute; top: 166px; width: 100%; text-align: center;
    font-family: "Michroma", sans-serif; font-size: 22px; letter-spacing: 1px;
  }
  .handprint {
    position: absolute; left: 40px; right: -10px; top: 250px; bottom: -10px;
    background: radial-gradient(ellipse at 50% 70%, var(--print-tone) 0%, rgba(255,255,255,0.12) 45%, transparent 75%);
  }
  .handprint.faint { left: -20px; right: 60px; top: 200px; opacity: 0.5; }
  /* back */
  .info {
    position: absolute; top: 78px; left: 34px; right: 40px;
    font-family: "Lato", sans-serif; font-weight: 700; font-size: 11.5px; line-height: 1.25;
    text-align: justify;
  }
  .info p { margin-bottom: 14px; }
  .info em { font-style: italic; }
  .cautions {
    font-weight: 400; font-size: 10px; list-style: none; text-align: left; line-height: 1.45;
  }
  .cautions-title { font-style: italic; font-weight: 700; font-size: 10px; margin-bottom: 2px; }
  .cautions li::before { content: "\2022"; margin-right: 5px; }
  .origin-badge {
    position: absolute; right: 30px; top: 392px;
    width: 60px; height: 60px; border-radius: 50%;
    background: var(--badge-fill); border: 3px solid var(--badge-ring);
  }
  .size-tag {
    position: absolute; bottom: 28px; left: 50%; transform: translateX(-50%);
    background: var(--size-tag); color: var(--size-tag-ink);
    font-family: "Lato", sans-serif; font-weight: 700; font-style: italic; font-size: 15px;
    padding: 1px 6px; border-radius: 3px;
  }
</style>
</head>
<body>
<main class="canvas">
  <section class="label label-front">
    <div class="handprint" role="img" aria-label="White distressed handprint illustration"></div>
    <span class="brand-mark" aria-hidden="true"></span>
    <h1 class="brand-name">VARNEL</h1>
    <h2 class="product-name">LIQUID CHALK</h2>
  </section>

  <section class="label label-back">
    <div class="handprint faint" role="img" aria-label="Faint white handprint texture"></div>
    <div class="info">
      <p>Made by USA Competitive Athletes for Athletes. Increases grip and lasts 3-4 times longer than regular chalk.</p>
      <p><em>Directions:</em> Shake well. Squeeze some Varnel Liquid Chalk into your hand and rub your hands together. Let your hands air dry for about 10 seconds. To remove the chalk wash your hands with light soap.</p>
      <p><em>Warning:</em> Avoid contact with Eyes. Do not use on broken skin. Do not ingest. Keep out of reach of small children.</p>
      <p>Ingredients: Magnesium carbonate, SD Alcohol, hydroxypropylcellulose, colophonium.</p>
      <p class="cautions-title">CAUTIONS:</p>
      <ul class="cautions">
        <li>For external use only.</li>
        <li>Avoid contact with eyes discontinue use if irritation develops.</li>
        <li>Keep out of reach of children</li>
        <li>Do not expose to open flame</li>
        <li>Store in a cool or dry place</li>
      </ul>
    </div>
    <span class="origin-badge" aria-hidden="true"></span>
    <span class="size-tag">50 ML</span>
  </section>
</main>
</body>
</html>
```